varnok llc

excavating and landscaping

Target Market(s)

Industry/Entity Type

Contact Information for Business Card

file atach

Font styles to use
Serif

```html
<!DOCTYPE html>
<html lang="en">
<head>
<meta charset="utf-8">
<title>Brantleys Backhoe Service – Business Card</title>
<link href="https://fonts.googleapis.com/css2?family=Cinzel:wght@600;700&family=Playfair+Display:ital,wght@1,600;1,800&display=swap" rel="stylesheet">
<style>
  :root {
    --stage: #6e6e6e;
    --card-red: #ff0000;
    --panel-black: #231f20;
    --ink-white: #ffffff;
    --badge-dark: #1a1a1a;
  }
  html, body {
    margin: 0;
    padding: 0;
    width: 1198px;
    height: 1200px;
    overflow: hidden;
    background: var(--stage);
  }
  .card {
    position: absolute;
    left: 69px;
    top: 303px;
    width: 1055px;
    height: 599px;
    background: var(--card-red);
    overflow: hidden;
  }
  .card__panel {
    position: absolute;
    left: 98px;
    top: 0;
    width: 957px;
    height: 389px;
    background: var(--panel-black);
  }
  .card__brand {
    position: absolute;
    left: 250px;
    top: 8px;
    margin: 0;
    font-family: "Playfair Display", Georgia, serif;
    font-style: italic;
    font-weight: 800;
    font-size: 118px;
    line-height: 1;
    letter-spacing: 1px;
    color: var(--ink-white);
  }
  .card__service {
    position: absolute;
    right: 60px;
    top: 124px;
    margin: 0;
    font-family: "Cinzel", Georgia, serif;
    font-weight: 700;
    font-size: 44px;
    line-height: 1;
    color: var(--card-red);
  }
  .card__contact {
    position: absolute;
    left: 838px;
    top: 195px;
    margin: 0;
    font-family: "Cinzel", Georgia, serif;
    font-weight: 700;
    font-size: 36px;
    line-height: 62px;
    color: var(--ink-white);
  }
  .card__since {
    position: absolute;
    left: 778px;
    top: 317px;
    margin: 0;
    font-family: "Playfair Display", Georgia, serif;
    font-style: italic;
    font-weight: 600;
    font-size: 42px;
    line-height: 1;
    color: var(--ink-white);
  }
  .card__logo {
    position: absolute;
    left: 30px;
    top: 10px;
    width: 560px;
    height: 540px;
  }
  .card__tagline {
    position: absolute;
    left: 0;
    right: 0;
    top: 526px;
    margin: 0;
    text-align: center;
    font-family: "Cinzel", Georgia, serif;
    font-weight: 700;
    font-size: 50px;
    line-height: 1;
    color: var(--ink-white);
  }
</style>
</head>
<body>
  <div class="card">
    <div class="card__panel"></div>

    <svg class="card__logo" viewBox="0 0 560 540" role="img" aria-label="Varnok LLC company mark">
      <circle cx="307" cy="353" r="172" fill="var(--badge-dark)"/>
      <text x="307" y="368" text-anchor="middle"
            font-family="Cinzel, Georgia, serif" font-weight="700" font-size="50"
            fill="#ffffff">VARNOK LLC</text>
    </svg>

    <h1 class="card__brand">BRANTLEYS</h1>
    <p class="card__service">Backhoe Service</p>
    <p class="card__contact">Name<br>Phone</p>
    <p class="card__since">Since ????</p>
    <p class="card__tagline">EXCAVATING AND LANDSCAPING</p>
  </div>
</body>
</html>
```